We need a tri-fold brochure for our business called: KindleSprout. (KindleSprout Therapy Services)
This is a therapy services business that offers Physiotherapy and Occupational Therapy to children aged 5 to 16 years of age. The focus is on Neuro-developmental therapy and the children have a range of conditions such as Cerebral-Palsy, brain injuries etc... We are looking for designs that focus on children, fun and the word nurture.
Target Market(s)
Primarily parents and people looking for therapy services.
Industry/Entity Type
Business
Font styles to use
Sans Serif

```html
<!DOCTYPE html>
<html lang="en">
<head>
<meta charset="utf-8">
<title>KindleSprout Therapy Services – Tri-fold Brochure</title>
<link rel="stylesheet" href="https://fonts.googleapis.com/css2?family=Exo+2:wght@400;500;600;700&display=swap">
<style>
  :root{
    --bg:#e4e4e7;
    --teal:#1f9489;
    --teal-dark:#16665f;
    --teal-deep:#0f524c;
    --teal-light:#3fbcae;
    --paper:#f4f4f4;
    --grey-band:#a3a3a5;
    --grey-mid:#cfcfd1;
    --ink:#4a4a4a;
    --white:#ffffff;
    --sprout:#9cc83c;
  }
  *{box-sizing:border-box;margin:0;padding:0}
  html,body{width:1200px;height:1000px;overflow:hidden}
  body{background:var(--bg);font-family:"Exo 2",sans-serif;position:relative}

  .panel{position:absolute;top:190px;height:620px;overflow:hidden;background:var(--paper);box-shadow:0 14px 30px rgba(0,0,0,.18)}

  /* Cover */
  .cover{left:40px;width:270px}
  .cover__header{position:absolute;left:0;top:0;width:100%;height:120px;background:var(--teal-dark);border-bottom:4px solid var(--teal-light)}
  .cover__brand{position:absolute;left:0;right:0;top:44px;text-align:center;color:var(--white);font-weight:600;font-size:30px;letter-spacing:.5px}
  .cover__brand::before{content:"";display:inline-block;width:14px;height:14px;border-radius:50%;background:var(--sprout);margin-right:10px;vertical-align:middle}
  .cover__band{position:absolute;left:0;top:124px;width:100%;height:150px;background:linear-gradient(180deg,var(--teal) 0%,var(--teal-light) 100%)}
  .cover__label{position:absolute;background:var(--teal-deep);color:var(--white);font-size:15px;font-weight:500;padding:7px 14px}
  .cover__label--name{left:0;top:14px;width:160px;padding-left:34px}
  .cover__label--tag{right:14px;top:52px}
  .cover__photo{position:absolute;left:0;top:250px;width:256px;height:170px;border-radius:0 26px 0 26px;background:linear-gradient(135deg,#d9cdb5,#8fa7a0 60%,#4b5a56)}
  .cover__prints{position:absolute;left:60px;top:455px;width:150px;height:90px;border-radius:14px;background:linear-gradient(90deg,#3cc4e6,#e0499b 40%,#f2d338 70%,#8bc43f)}
  .cover__footer{position:absolute;left:0;bottom:0;width:100%;height:58px;background:var(--grey-band);display:flex;justify-content:center;align-items:center;gap:14px}
  .social-dot{width:18px;height:18px;border-radius:50%;background:var(--white)}

  /* Inside spread */
  .spread{left:340px;width:820px;background:linear-gradient(180deg,var(--teal-dark) 0%,var(--teal) 24%,var(--teal-light) 40%,var(--paper) 52%,var(--paper) 100%)}
  .spread__col{position:absolute;top:0;width:273px;height:100%}
  .spread__col--who{left:0}
  .spread__col--services{left:273px;background:linear-gradient(180deg,rgba(0,0,0,.12),rgba(0,0,0,0) 30%)}
  .spread__col--guides{left:546px}
  .spread__col + .spread__col{border-left:1px solid rgba(0,0,0,.08)}
  .spread__title{position:absolute;left:0;right:0;top:40px;text-align:center;color:var(--white);font-weight:600;font-size:24px;letter-spacing:.5px}
  .spread__text{position:absolute;left:20px;right:20px;top:100px;color:var(--white);font-size:14px;line-height:1.35}
  .spread__footer{position:absolute;left:0;bottom:0;width:820px;height:56px;background:var(--grey-band)}

  .who__photo{position:absolute;left:20px;right:20px;top:330px;height:170px;border-radius:20px 0 20px 0;background:linear-gradient(135deg,#6b6f86,#c9b7a8 55%,#3d3a44)}

  .service{position:absolute;left:14px;width:245px;height:115px}
  .service--physio{top:105px}.service--ot{top:240px}.service--neuro{top:375px}
  .service__photo{position:absolute;left:0;top:0;width:90px;height:115px;border-radius:16px 0 0 16px;background:linear-gradient(135deg,#a7c9b9,#d7b88a 60%,#6c8f83)}
  .service__card{position:absolute;left:72px;top:0;width:173px;height:115px;background:var(--white);border-radius:0 16px 0 16px;box-shadow:0 3px 6px rgba(0,0,0,.25);padding:8px 10px;color:var(--ink)}
  .service__name{font-size:10px;font-weight:700;text-align:center;text-transform:uppercase;line-height:1.2}
  .service__icon{display:block;margin:4px auto 4px;border-top:1px solid #ddd;padding-top:4px;width:100%;height:16px}
  .service__desc{font-size:7px;line-height:1.3}

  .guides__tab{position:absolute;left:18px;top:300px;width:44px;height:240px;background:#6f8f92;border-radius:10px;display:flex;align-items:center;justify-content:center}
  .guides__tab span{transform:rotate(-90deg);white-space:nowrap;color:var(--white);font-size:19px;font-weight:500;letter-spacing:2px}
  .guides__photo{position:absolute;left:76px;right:16px;top:300px;height:150px;border-radius:14px;background:linear-gradient(135deg,#5da6c9,#c77d45 55%,#8a3a52)}
  .guides__prints{position:absolute;left:86px;top:460px;width:150px;height:80px;border-radius:14px;background:linear-gradient(90deg,#f2d338,#8bc43f 35%,#e0499b 65%,#3cc4e6)}
</style>
</head>
<body>

<section class="panel cover" aria-label="Front cover">
  <header class="cover__header">
    <div class="cover__brand">KindleSprout</div>
  </header>
  <div class="cover__band">
    <div class="cover__label cover__label--name">KindleSprout</div>
    <div class="cover__label cover__label--tag">Therapy Services</div>
  </div>
  <div class="cover__photo" role="img" aria-label="Photo of a smiling young boy seated in a supportive wheelchair in a classroom"></div>
  <div class="cover__prints" role="img" aria-label="Colourful paint handprints in blue, pink, yellow and green"></div>
  <footer class="cover__footer">
    <span class="social-dot"></span><span class="social-dot"></span><span class="social-dot"></span><span class="social-dot"></span>
  </footer>
</section>

<section class="panel spread" aria-label="Inside spread">
  <div class="spread__col spread__col--who">
    <h2 class="spread__title">WHO ARE WE?</h2>
    <p class="spread__text">Lorem ipsum dolor sit amet, consectetuer adipiscing elit, sed diam nonummy nibh euismod tincidunt ut laoreet dolore magna aliquam erat volutpat. Lorem ipsum dolor sit amet, consectetuer adipiscing elit.</p>
    <div class="who__photo" role="img" aria-label="Photo of a therapist playing with a young child on a mat"></div>
  </div>

  <div class="spread__col spread__col--services">
    <h2 class="spread__title">OUR SERVICES</h2>

    <article class="service service--physio">
      <div class="service__photo" role="img" aria-label="Photo of a physiotherapist guiding a child on an exercise ball"></div>
      <div class="service__card">
        <h3 class="service__name">Physiotherapy</h3>
        <svg class="service__icon" viewBox="0 0 150 16"><rect x="68" y="4" width="14" height="9" rx="2" fill="none" stroke="#7bbf9a" stroke-width="1.3"/></svg>
        <p class="service__desc">Play-based sessions build strength, balance and confident movement, helping each child move with more ease at home, at school and with friends.</p>
      </div>
    </article>

    <article class="service service--ot">
      <div class="service__photo" role="img" aria-label="Photo of a therapist doing a craft activity with a child"></div>
      <div class="service__card">
        <h3 class="service__name">Occupational<br>Therapy</h3>
        <svg class="service__icon" viewBox="0 0 150 16"><rect x="69" y="2" width="12" height="12" rx="2" fill="none" stroke="#5a8fa8" stroke-width="1.3"/><path d="M72 11 L79 4" stroke="#5a8fa8" stroke-width="1.3"/></svg>
        <p class="service__desc">We build everyday skills like dressing, writing and eating, so children gain independence through creative tasks they truly enjoy doing.</p>
      </div>
    </article>

    <article class="service service--neuro">
      <div class="service__photo" role="img" aria-label="Photo of a therapist and toddler playing with a bead maze toy"></div>
      <div class="service__card">
        <h3 class="service__name">Neuro Therapy</h3>
        <svg class="service__icon" viewBox="0 0 150 16"><circle cx="73" cy="6" r="3" fill="none" stroke="#666" stroke-width="1.2"/><path d="M68 14 Q73 8 78 14" fill="none" stroke="#666" stroke-width="1.2"/><circle cx="80" cy="7" r="2" fill="none" stroke="#666" stroke-width="1"/></svg>
        <p class="service__desc">Neuro-developmental therapy supports children with cerebral palsy or brain injury, guiding posture, control and coordination step by step.</p>
      </div>
    </article>
  </div>

  <div class="spread__col spread__col--guides">
    <h2 class="spread__title">OUR GUIDELINES</h2>
    <p class="spread__text">Lorem ipsum dolor sit amet, consectetuer adipiscing elit, sed diam nonummy nibh euismod tincidunt ut laoreet dolore Lorem ipsum dolor sit amet, consectetuer adipiscing elit, sed</p>
    <div class="guides__tab"><span>KINDLESPROUT</span></div>
    <div class="guides__photo" role="img" aria-label="Photo of a laughing father with his son in a wheelchair"></div>
    <div class="guides__prints" role="img" aria-label="Colourful paint handprints in yellow, green, pink and blue"></div>
  </div>

  <div class="spread__footer"></div>
</section>

</body>
</html>
```